CPA Firm Stationary & Business Cards
Whitfield & Partners CPAs PSC
CPA Firm Stationary & Business Cards - Financial Services
Creative Brief
Professional
Martin L. Dowse, CPA
Shareholder
4815 Tillamore Ave. Suite 1 Owensboro, KY 42303
mdowse@wpfcpa.net
www.wpfcpa.net
We are a CPA (Certified Public Accountant) firm, in business since 1924. In addition to Business Cards, I would also like to see designs for Letterheads and Envelopes.
Your choice. At a minimum, it should include the "W" logo.In addition to Business Cards, I would also like to see designs for Letterheads and Envelopes.

```html
<!DOCTYPE html>
<html lang="en">
<head>
<meta charset="utf-8">
<title>Whitfield & Partners CPAs PSC – Stationery</title>
<link href="https://fonts.googleapis.com/css2?family=Roboto:wght@400;700&display=swap" rel="stylesheet">
<style>
  :root{
    --bg:#000000;
    --paper:#ffffff;
    --blue:#1a5fc8;
    --blue-deep:#0c3688;
    --grey:#8b9099;
    --ink:#2a2f3a;
    --faint:#eef1f6;
  }
  html,body{margin:0;padding:0;overflow:hidden;background:var(--bg);}
  .canvas{position:relative;width:1200px;height:523px;overflow:hidden;background:var(--bg);font-family:"Roboto",Arial,sans-serif;}
  .piece{position:absolute;display:block;}
  .piece text{font-family:"Roboto",Arial,sans-serif;}
  .card-front{left:67px;top:223px;width:125px;height:50px;}
  .card-back{left:67px;top:300px;width:125px;height:50px;}
  .card-blue{left:67px;top:377px;width:125px;height:50px;}
  .letterhead-cover{left:204px;top:65px;width:295px;height:381px;}
  .letterhead-main{left:511px;top:65px;width:295px;height:381px;}
  .envelope-back{left:816px;top:151px;width:314px;height:135px;}
  .envelope-front{left:816px;top:302px;width:314px;height:147px;}
</style>
</head>
<body>
<main class="canvas">
  <svg width="0" height="0" style="position:absolute">
    <defs>
      <linearGradient id="brand-blue" x1="0" y1="0" x2="1" y2="1">
        <stop offset="0" stop-color="var(--blue)"/>
        <stop offset="1" stop-color="var(--blue-deep)"/>
      </linearGradient>
    </defs>
  </svg>

  <!-- Business card, front -->
  <svg class="piece card-front" viewBox="0 0 125 50">
    <rect width="125" height="50" fill="var(--paper)"/>
    <path d="M50 0 H125 V14 C100 8 75 4 50 0Z" fill="url(#brand-blue)"/>
    <path d="M45 0 C75 5 100 10 125 17" fill="none" stroke="var(--grey)" stroke-width="1.2"/>
    <circle cx="10" cy="22" r="2.5" fill="var(--blue)"/>
    <text x="15" y="24" font-size="5" font-weight="700" fill="var(--blue)">Whitfield &amp; Partners</text>
    <text x="10" y="34" font-size="3.4" fill="var(--ink)">Martin L. Dowse, CPA</text>
    <text x="10" y="38.5" font-size="2.8" fill="var(--grey)">Shareholder</text>
  </svg>

  <!-- Business card, details -->
  <svg class="piece card-back" viewBox="0 0 125 50">
    <rect width="125" height="50" fill="var(--paper)"/>
    <path d="M0 40 C40 38 90 34 125 26 V50 H0Z" fill="url(#brand-blue)"/>
    <path d="M0 37 C40 35 90 31 125 23" fill="none" stroke="var(--grey)" stroke-width="1"/>
    <text x="8" y="11" font-size="3.4" font-weight="700" fill="var(--ink)">Martin L. Dowse, CPA</text>
    <text x="8" y="15.5" font-size="2.6" fill="var(--grey)">Shareholder</text>
    <text x="8" y="22" font-size="2.4" fill="var(--ink)">Tel 270.555.0142</text>
    <text x="8" y="26" font-size="2.4" fill="var(--ink)">mdowse@wpfcpa.net</text>
    <text x="8" y="47" font-size="2.4" fill="var(--paper)">www.wpfcpa.net</text>
  </svg>

  <!-- Business card, blue reverse -->
  <svg class="piece card-blue" viewBox="0 0 125 50">
    <rect width="125" height="50" fill="url(#brand-blue)"/>
    <path d="M0 30 C40 28 90 24 125 16" fill="none" stroke="var(--paper)" stroke-opacity=".35" stroke-width="1"/>
    <text x="8" y="43" font-size="2.6" fill="var(--paper)">www.wpfcpa.net</text>
  </svg>

  <!-- Letterhead, cover sheet -->
  <svg class="piece letterhead-cover" viewBox="0 0 295 381">
    <rect width="295" height="381" fill="var(--paper)"/>
    <circle cx="150" cy="185" r="60" fill="var(--faint)"/>
    <path d="M105 0 H295 V44 C230 22 165 8 105 0Z" fill="url(#brand-blue)"/>
    <path d="M95 0 C165 9 235 25 295 50" fill="none" stroke="var(--grey)" stroke-width="3"/>
    <text x="244" y="10" font-size="3.6" fill="var(--paper)">4815 Tillamore Ave. Suite 1</text>
    <text x="244" y="15" font-size="3.6" fill="var(--paper)">Owensboro, KY 42303</text>
    <text x="244" y="20" font-size="3.6" fill="var(--paper)">Tel 270.555.0142</text>
    <text x="244" y="25" font-size="3.6" fill="var(--paper)">www.wpfcpa.net</text>
  </svg>

  <!-- Letterhead, main sheet -->
  <svg class="piece letterhead-main" viewBox="0 0 295 381">
    <rect width="295" height="381" fill="var(--paper)"/>
    <circle cx="148" cy="185" r="60" fill="var(--faint)"/>
    <circle cx="106" cy="34" r="4" fill="var(--blue)"/>
    <text x="113" y="37" font-size="8" font-weight="700" fill="var(--blue)">Whitfield &amp; Partners</text>
    <text x="113" y="43" font-size="3.4" fill="var(--grey)">Whitfield &amp; Partners CPAs PSC</text>
    <path d="M0 352 C90 350 200 335 295 300 V381 H0Z" fill="url(#brand-blue)"/>
    <path d="M0 343 C90 341 200 326 295 290" fill="none" stroke="var(--grey)" stroke-width="3"/>
    <text x="147" y="372" font-size="3.6" fill="var(--paper)" text-anchor="middle">4815 Tillamore Ave. Suite 1 · Owensboro, KY 42303 · Tel 270.555.0142 · www.wpfcpa.net</text>
  </svg>

  <!-- Envelope, back with flap -->
  <svg class="piece envelope-back" viewBox="0 0 314 135">
    <rect width="314" height="135" fill="var(--paper)"/>
    <path d="M0 0 H314 V40 Q300 54 280 54 H34 Q14 54 0 40Z" fill="url(#brand-blue)"/>
    <circle cx="133" cy="27" r="4" fill="var(--paper)"/>
    <text x="140" y="30" font-size="8" font-weight="700" fill="var(--paper)">Whitfield</text>
  </svg>

  <!-- Envelope, front -->
  <svg class="piece envelope-front" viewBox="0 0 314 147">
    <rect width="314" height="147" fill="var(--paper)"/>
    <path d="M110 0 H314 V30 C250 14 180 5 110 0Z" fill="url(#brand-blue)"/>
    <path d="M100 0 C180 6 250 18 314 38" fill="none" stroke="var(--grey)" stroke-width="3"/>
    <text x="268" y="11" font-size="3.4" fill="var(--paper)">Tel 270.555.0142</text>
    <text x="268" y="16" font-size="3.4" fill="var(--paper)">www.wpfcpa.net</text>
    <circle cx="13" cy="46" r="4" fill="var(--blue)"/>
    <text x="20" y="49" font-size="7" font-weight="700" fill="var(--blue)">Whitfield &amp; Partners</text>
    <text x="20" y="55" font-size="3.2" fill="var(--grey)">4815 Tillamore Ave. Suite 1</text>
  </svg>
</main>
</body>
</html>
```